Maple Ridge Power Process Graphic

I need a graphic that outlines the 4 step process to have a solar energy system installed.

1. Get Started - Our solar experts will analyze your electric consumption and work with you to choose the system and plan that works best for your home
2. System Design - Our engineers will custom design a system to meet your electric needs and draft your architectural plans so we can obtain your permit
3. Permitting, Installation, & Inspection - We will work with your local building department and utility to get all of the required permits and permissions for your solar energy system installation. We will also take care of the required inspections so that you don't have to!
4. Power On - We will walk you through your new solar energy system, set up your monitoring system on your smartphone or computer, and then the most fun part- power on your system and watch your meter spin backwards!

You can find examples of similar graphics at brightfield.example, lumatech.example, and glowgrid.example.

All of the text is not required in the graphic as I want a clean look and feel, but the nuts and bolts should be included. I have attached our logo so you have a feel for the branding. I would like a simple graphic for each step that depicts what we will be accomplishing during that step. Please message me with any inquiries.

Target Market(s)

Residential customers

Industry/Entity Type

Solar Energy

Font styles to use
Sans Serif

Requirements
Must have
• 4 simple graphics using colors from our logo to depict the process described in the project description
Nice to have
• Text that matches our logo branding to briefly describe the process, see description for details. Try to match similar text style to logo
Should not have
• Should not be overly complex

```html
<!DOCTYPE html>
<html lang="en">
<head>
<meta charset="utf-8">
<title>Maple Ridge Power – Solar Installation Process</title>
<link rel="stylesheet" href="https://fonts.googleapis.com/css2?family=Playfair+Display:wght@700&family=Raleway:wght@500&display=swap">
<style>
  :root {
    --ink: #2b2b2b;
    --title-grey: #6b6b6b;
    --title-dark: #4a4a4a;
    --sky-light: #d8eefa;
    --sky: #a9dcf6;
    --cyan: #2bb6e6;
    --leaf-light: #e6f4d4;
    --leaf: #b9df8a;
    --sun-light: #fff6b8;
    --sun: #ffe500;
    --slate-light: #dcdcdc;
    --slate: #bdbdbd;
    --placeholder-warm: #e9b3b5;
    --white: #ffffff;
  }
  * { box-sizing: border-box; margin: 0; padding: 0; }
  html, body { width: 851px; height: 1200px; overflow: hidden; background: var(--white); }
  .process {
    position: relative;
    width: 851px;
    height: 1200px;
    font-family: "Raleway", sans-serif;
    color: var(--ink);
  }
  .step { position: absolute; left: 0; width: 851px; overflow: hidden; }
  .step-title {
    font-family: "Playfair Display", serif;
    font-weight: 700;
    line-height: 1.05;
  }
  .step-text { font-size: 23px; line-height: 1.42; }
  .art { position: absolute; }

  /* Step 1 */
  .step--start {
    top: 0; height: 278px;
    background: linear-gradient(160deg, var(--white) 0%, var(--sky-light) 35%, var(--sky) 100%);
  }
  .step--start .art { left: 0; top: 0; width: 110px; height: 278px;
    background: linear-gradient(180deg, var(--white), #eaf6fd); }
  .step--start .step-title { position: absolute; right: 26px; top: 30px; font-size: 56px; color: var(--title-grey); }
  .step--start .step-text { position: absolute; left: 362px; right: 20px; top: 112px; }

  /* Step 2 */
  .step--design { top: 300px; height: 250px; background: var(--white); }
  .step--design .band { position: absolute; left: 0; top: 0; width: 552px; height: 250px;
    background: linear-gradient(180deg, var(--cyan) 0 88px, var(--sky-light) 88px); }
  .step--design .step-title { position: absolute; left: 18px; top: 16px; font-size: 56px; color: var(--ink); }
  .step--design .step-text { position: absolute; left: 18px; width: 520px; top: 100px; }
  .step--design .art { left: 570px; top: 30px; width: 262px; height: 190px;
    background: linear-gradient(135deg, var(--leaf-light), var(--leaf)); }

  /* Step 3 */
  .step--permit { top: 578px; height: 338px; background: var(--sun-light); }
  .step--permit .art { left: 0; top: 0; width: 250px; height: 338px; background: var(--sun); }
  .step--permit .step-title { position: absolute; left: 260px; right: 14px; top: 14px; font-size: 44px; color: var(--title-grey); text-align: right; }
  .step--permit .step-text { position: absolute; left: 266px; right: 16px; top: 120px; text-align: center; font-size: 19.5px; line-height: 1.4; }

  /* Step 4 */
  .step--power {
    top: 944px; height: 256px;
    background: linear-gradient(180deg, var(--slate-light), var(--slate));
  }
  .step--power .step-title { position: absolute; left: 22px; top: 14px; font-size: 56px; color: var(--title-dark); }
  .step--power .step-text { position: absolute; left: 22px; width: 610px; top: 90px; font-size: 20.5px; line-height: 1.4; }
  .step--power .art { left: 650px; top: 40px; width: 180px; height: 176px;
    background: linear-gradient(160deg, var(--slate-light), var(--placeholder-warm)); }
</style>
</head>
<body>
<main class="process">

  <section class="step step--start">
    <div class="art" role="img" aria-label="Hand-drawn letters S T A R T stacked vertically in blue boxes"></div>
    <h2 class="step-title">Get Started</h2>
    <p class="step-text">Our solar experts will analyze your electric consumption and work with you to choose the system and plan that works best for your home.</p>
  </section>

  <section class="step step--design">
    <div class="band"></div>
    <h2 class="step-title">System Design</h2>
    <p class="step-text">Our engineers will custom design a system to meet your electric needs and draft your architectural plans so we can obtain your permit.</p>
    <div class="art" role="img" aria-label="Green circuit-board lines ending in small circles"></div>
  </section>

  <section class="step step--permit">
    <div class="art" role="img" aria-label="Blue sketch of a signed permit document and a wrench on yellow"></div>
    <h2 class="step-title">Permitting, Installation,<br>&amp; Inspection</h2>
    <p class="step-text">We will work with your local building department and utility to get all of the required permits and permissions for your solar energy system installation. We will also take care of the required inspections so that you don’t have to!</p>
  </section>

  <section class="step step--power">
    <h2 class="step-title">Power On</h2>
    <p class="step-text">We will walk you through your new solar energy system, set up your monitoring system on your smartphone or computer, and then the most fun part- power on your system and watch your meter spin backwards!</p>
    <div class="art" role="img" aria-label="Illustration of a red power button marked ON"></div>
  </section>

</main>
</body>
</html>
```